A website for a green bio-plastics manufacturing company

We need a home page designed and two complimentary template pages that can be used for the rest of the website. The template page should vary in design from the home page, but should flow uniformly with it.

This is a very innovative company with a proprietary manufacturing method of using bird feathers to make plastic.

The site should be functional, informative, user-friendly and informative to both our business partners and the consumers.
Updates

I've added a more concise overview of the company.  If any of the designers have any questions for me, please ask.  Thanks

Marco

Target Market(s)

Business partners interested in using bio-plastics for their products and general customers.

Industry/Entity Type

Manufacturing

Number of Pages Required

3 pages

Requirements
Must have
• I attached some information about the company, so the site should be designed to incorporate that content.

Will need to be edited by Adobe Contribute.

Easy to navigate

One of the template pages should have one column for content. The other should have two columns. I''m open to different ideas though.

Should be very pleasing to the eye and uncluttered.

Want to be informative to both our business partners as well as consumers who may be researching our product(s)

Easy to Maintain

Anticipated Tabs/Pages
· Home Page
o General “welcome” page

· About Us
o Company overview and information

· Products
o Horticulture Containers
o Agriculture Films
o Where to Buy
o Upcoming Products

· Business Partners

· Press Releases

· Contact Us

Nice to have
• Would like to have earth tones and or nice greens in the color scheme. They make use of bird feathers for their manufacturing process, so perhaps a real sharp image of a feather can be incorporated into the design. Be creative though.

Perhaps a jQuery nav bar, but that may be out of scope.

Should not have
• No flash at all.

```html
<!DOCTYPE html>
<html lang="en">
<head>
<meta charset="utf-8">
<title>Verdant BioPlastics – Home</title>
<link rel="stylesheet" href="https://fonts.googleapis.com/css2?family=Arimo:ital,wght@0,400;0,700;1,400;1,700&display=swap">
<style>
:root{
  --page-green:#a9c433;
  --leaf-dark:#6f8c22;
  --leaf-mid:#9ab82a;
  --olive-text:#3d5a0c;
  --ink:#222;
  --body-text:#555;
  --card:#fff;
  --rule:#d6d6d6;
  --sky:#9cc7e6;
  --meadow:#7fb32a;
}
*{margin:0;padding:0;box-sizing:border-box}
html,body{width:1108px;height:1200px;overflow:hidden}
body{background:var(--page-green);font-family:"Arimo",Arial,sans-serif;position:relative;color:var(--ink)}
.abs{position:absolute}
.card{left:111px;top:145px;width:886px;height:919px;background:var(--card);border-radius:6px;overflow:hidden}
.sidebar-shade{left:0;width:328px;background:linear-gradient(90deg,#fff 60%,#ececec)}
.brand{left:145px;top:198px;display:flex;align-items:center;gap:10px}
.brand-mark{width:44px;height:44px;border-radius:50%;background:var(--leaf-dark)}
.brand-name{font-size:26px;font-weight:700;color:var(--leaf-dark);line-height:1}
.main-nav{left:436px;top:196px;display:flex;height:54px}
.main-nav a{display:flex;align-items:center;padding:0 6px;border-left:1px solid var(--leaf-mid);font-size:12.5px;font-weight:700;color:#444;text-decoration:none;height:100%}
.hero{left:111px;top:238px;width:886px;height:262px}
.hero-title{left:486px;top:286px;font-weight:700;color:#111;font-size:25px;line-height:31px}
.hero-title .t2{display:block;padding-left:14px}
.hero-title .t3{display:block;padding-left:36px;font-size:40px;line-height:50px;color:var(--olive-text)}
.btn{display:flex;align-items:center;justify-content:center;background:var(--leaf-dark);color:#fff;font-weight:700;border-radius:3px;box-shadow:0 1px 2px rgba(0,0,0,.3)}
.partner{background:var(--leaf-mid)}
.donate-note{left:137px;top:832px;font-size:17px;font-weight:700;color:#555}
.signup-note{left:128px;top:982px;font-size:14px;font-style:italic;font-weight:700;color:#444}
.email-field{left:142px;top:1012px;width:185px;height:17px;border:1px solid #333;font-size:14px;font-style:italic;font-weight:700;color:var(--leaf-mid);padding-left:12px;line-height:15px}
.submit{left:331px;top:1012px;width:76px;height:17px;background:var(--leaf-mid);color:#fff;font-size:10px;display:flex;align-items:center;justify-content:center}
.col-rule{left:441px;top:474px;width:2px;height:590px;background:var(--leaf-mid)}
.section-title{left:470px;top:500px;font-size:15px;font-weight:700;font-style:italic;color:var(--leaf-mid)}
.about-text{left:468px;top:519px;width:245px;font-size:11px;line-height:18.5px;color:var(--body-text)}
.featured-label{left:782px;top:494px;font-size:12px;font-weight:700;font-style:italic;color:var(--leaf-dark)}
.featured-photo{left:751px;top:516px;width:194px;height:160px;background:linear-gradient(180deg,var(--sky),#d9ecf5 55%,var(--meadow))}
.plan-text{left:467px;top:693px;width:480px;font-size:11px;line-height:19.4px;color:var(--body-text)}
.highlight{left:468px;top:795px;width:470px;font-size:11px;line-height:15px;color:var(--body-text)}
.highlight b{color:var(--leaf-mid)}
.link-list{left:476px;top:852px;list-style:none;font-size:11px;line-height:15.6px;color:#555}
.link-list li::before{content:"";display:inline-block;border-left:4px solid #333;border-top:3px solid transparent;border-bottom:3px solid transparent;margin-right:8px;vertical-align:1px}
.footer-links{left:121px;top:1077px;display:flex;gap:8px;font-size:10px;color:#fff}
.follow{left:776px;top:1083px;font-size:14px;font-weight:700;color:#fff}
.social{top:1073px;width:34px;height:34px;border-radius:4px;background:#3b5aa0}
</style>
</head>
<body>
<div class="abs card">
  <div class="abs sidebar-shade" style="top:355px;height:250px"></div>
  <div class="abs sidebar-shade" style="top:755px;height:175px"></div>
</div>

<div class="abs brand"><span class="brand-mark"></span><span class="brand-name">Verdant BioPlastics</span></div>

<nav class="abs main-nav">
  <a>Objective</a><a>Mission</a><a>Our Inspiration</a><a>OurPhilosophy</a><a>Service</a><a>Providers</a><a style="border-right:0">The Founders</a>
</nav>

<svg class="abs hero" viewBox="0 0 886 262" aria-hidden="false">
  <defs>
    <linearGradient id="leafGlow" x1="0" y1="0" x2="1" y2="1">
      <stop offset="0" stop-color="#c9e07a"/><stop offset=".5" stop-color="#7fb32a"/><stop offset="1" stop-color="#a6cf4a"/>
    </linearGradient>
    <linearGradient id="meadowSky" x1="0" y1="0" x2="0" y2="1">
      <stop offset="0" stop-color="#cfe6f2"/><stop offset=".45" stop-color="#b9d98a"/><stop offset="1" stop-color="#8cbf2e"/>
    </linearGradient>
  </defs>
  <path role="img" aria-label="Photo of a child blowing a dandelion in a meadow" d="M0 20 Q160 60 328 48 L328 250 Q170 250 0 240 Z" fill="url(#meadowSky)"/>
  <path role="img" aria-label="Close-up photo of a green leaf with dew" d="M328 48 Q600 0 886 78 L886 290 Q640 200 328 250 Z" fill="url(#leafGlow)"/>
</svg>

<h1 class="abs hero-title">Become the leading<span class="t2">manufacturer and &nbsp;distributor of</span><span class="t3">bioplastics in the world</span></h1>

<div class="abs btn" style="left:136px;top:497px;width:172px;height:38px;font-size:16px">Business Partners</div>
<div class="abs partner" style="left:158px;top:554px;width:160px;height:46px;border-radius:4px"></div>
<div class="abs partner" style="left:188px;top:606px;width:62px;height:62px;border-radius:50%"></div>
<div class="abs partner" style="left:174px;top:683px;width:92px;height:61px;background:#f39a3a"></div>

<div class="abs btn" style="left:140px;top:780px;width:172px;height:39px;font-size:24px">Donate Now</div>
<div class="abs donate-note">Download a donate form</div>

<div class="abs btn" style="left:140px;top:912px;width:172px;height:38px;font-size:24px">Join Us</div>
<div class="abs signup-note">get updates, be involved and &nbsp;win great prize</div>
<div class="abs email-field">Email</div>
<div class="abs submit">Submit</div>

<div class="abs col-rule"></div>

<h2 class="abs section-title">About Us</h2>
<p class="abs about-text">Verdant BioPlastics is a green-technology start-up company that has implemented cutting edge technology and custom-designed machines to manufacture bioplastics from poultry feathers on an industrial scale. Marco Lindqvist, who brings a wealth of experience in agriculture, poultry, and business, is the entrepreneur behind the company’s creation and development.</p>

<div class="abs featured-label">Featured Projects</div>
<svg class="abs" style="left:722px;top:588px" width="18" height="22"><path d="M18 0 L0 11 L18 22 Z" fill="var(--leaf-dark)"/></svg>
<div class="abs featured-photo" role="img" aria-label="Photo of cupped hands holding a small tree seedling"></div>
<svg class="abs" style="left:951px;top:588px" width="18" height="22"><path d="M0 0 L18 11 L0 22 Z" fill="var(--leaf-dark)"/></svg>

<p class="abs plan-text">Verdant BioPlastics plans to manufacture virgin keratin-based resins and both sell these resins and further compound them to meet desired specifications. We plan to sell manufactured and compounded resins to our business partners who will further process these resins into end user products such as: greenhouse/nursery containers, agricultural films, automotive components, and/or office furniture.</p>

<p class="abs highlight"><b>Verdant BioPlastics is a green-technology start-up company that has implemented cuttingedge technol</b> &nbsp;and custom-esigned machines to manufacture bioplastics from poultry feathers on an industrial scale.</p>

<ul class="abs link-list">
  <li>Vision Statement</li><li>Mission Statement</li><li>Core Values &amp; Beliefs</li><li>Business Goals</li><li>Product</li>
</ul>

<div class="abs btn" style="left:780px;top:993px;width:172px;height:39px;font-size:14px;font-weight:400">More About Our program</div>

<div class="abs footer-links"><span>Home Page</span><span>FAQ</span><span>About us</span><span>Locations</span><span>Contact Us</span></div>
<div class="abs follow">follow us :</div>
<div class="abs social" style="left:862px"></div>
<div class="abs social" style="left:901px;background:#4fb6e0"></div>
<div class="abs social" style="left:940px;background:#1f3a6b"></div>
</body>
</html>
```